we need a business card design for a professional painting business. This company has been up and going for about ten years. However it needs an new logo. we want this business card to be modern eye catching and easy to read. I currently have been looking for VP logos but can not find one that suits our needs. This Design should be Our start to a new beginning.
Industry/Entity Type
Painting
Contact Information for Business Card
Varesko Painting Inc.
Licensed & Insured
Tomas Varesko
Phone(631)384-4562
Fax (555) 846-3021
E-mail vareskopaintinginc@mailorbit.test
Requirements
Must have
- a new logo with  VP and i would like it to be in black and white.
i would also like the front to be a solid black with the logo only and then the back to have the information.

```html
<!DOCTYPE html>
<html lang="en">
<head>
<meta charset="utf-8">
<title>Varesko Painting Inc. – Business Card</title>
<link href="https://fonts.googleapis.com/css2?family=Open+Sans:wght@400;600&display=swap" rel="stylesheet">
<style>
  :root {
    --backdrop: #e6e6e6;
    --ink: #1f1c1c;
    --paper: #f2f2f2;
    --white: #ffffff;
    --text-dark: #2a2a2a;
  }
  html, body {
    margin: 0;
    padding: 0;
    width: 1200px;
    height: 900px;
    overflow: hidden;
    background: var(--backdrop);
    font-family: "Open Sans", Arial, sans-serif;
  }
  .canvas {
    position: relative;
    width: 1200px;
    height: 900px;
  }
  .card {
    position: absolute;
    top: 310px;
    width: 490px;
    height: 280px;
    box-shadow: 0 6px 18px rgba(0,0,0,0.18);
    overflow: hidden;
  }
  .card-front {
    left: 90px;
    background: var(--ink);
    display: flex;
    align-items: center;
    justify-content: center;
  }
  .brand-mark {
    display: flex;
    align-items: center;
    gap: 14px;
    color: var(--white);
    font-weight: 600;
    font-size: 30px;
    letter-spacing: 0.5px;
  }
  .brand-square {
    width: 26px;
    height: 26px;
    background: var(--white);
  }
  .card-back {
    left: 620px;
    background: var(--paper);
  }
  .name-band {
    position: absolute;
    left: 0;
    top: 22px;
    width: 300px;
    height: 78px;
    background: var(--ink);
    color: var(--white);
    padding: 14px 0 0 22px;
    box-sizing: border-box;
  }
  .company-name {
    margin: 0;
    font-size: 17px;
    font-weight: 400;
    letter-spacing: 0.3px;
  }
  .tagline {
    margin: 4px 0 0;
    font-size: 11.5px;
    letter-spacing: 0.3px;
  }
  .contact-list {
    position: absolute;
    left: 130px;
    top: 150px;
    margin: 0;
    padding: 0;
    list-style: none;
    color: var(--text-dark);
    font-size: 14px;
    line-height: 22px;
    letter-spacing: 0.4px;
  }
</style>
</head>
<body>
  <main class="canvas">
    <section class="card card-front" aria-label="Card front">
      <div class="brand-mark">
        <span class="brand-square"></span>
        <span class="brand-name">Varesko Painting</span>
      </div>
    </section>

    <section class="card card-back" aria-label="Card back">
      <div class="name-band">
        <h1 class="company-name">Varesko Painting Inc.</h1>
        <p class="tagline">Licensed &amp; Insured Tomas Varesko</p>
      </div>
      <ul class="contact-list">
        <li>Phone (555)217-9083</li>
        <li>Fax (555) 846-3021</li>
        <li>vareskopaintinginc@mailorbit.test</li>
      </ul>
    </section>
  </main>
</body>
</html>
```